New Company Business Card Design

I have a new company logo and I want a new business card design. I dont know if the logo file i attached is in the correct format or quality. We are a New York City Specialty construction Firm specializing in high risk out of the box projects. I want a simple and classy business card that people will his card is as crisp as the work his company does.

Target Market(s)

Clients in the heavy construction industry in New York City

Industry/Entity Type

Construction Company

Contact Information for Business Card

Simple Classy - DIFFERENT

Font styles to use
Other font styles liked:
• Mach the logo font in some way

Colors

Designer to choose colors to be used in the design.

Requirements
Must have
• Uniqueness
Nice to have
• Nothing particular - Just different and classy - Timeless
Should not have
• Goofy Shit or Gimmicky shit

```html
<!DOCTYPE html>
<html lang="en">
<head>
<meta charset="utf-8">
<title>KRT Builders, Inc. — Business Card</title>
<link href="https://fonts.googleapis.com/css2?family=Arimo:wght@400;700&display=swap" rel="stylesheet">
<style>
  :root {
    --brand-blue: #1b75bb;
    --brand-deep: #0a4f94;
    --brand-light: #5fa6dc;
    --icon-blue: #29a8e0;
    --accent-orange: #f26a25;
    --ink: #1a1a1a;
    --paper: #ffffff;
  }
  * { margin: 0; padding: 0; box-sizing: border-box; }
  html, body { width: 1200px; height: 1200px; overflow: hidden; background: var(--paper); }
  body { position: relative; font-family: "Arimo", Arial, sans-serif; color: var(--ink); }

  .brand-mark {
    position: absolute; display: flex; align-items: center; gap: 16px;
    font-weight: 700; color: var(--brand-blue); white-space: nowrap;
  }
  .brand-mark .brand-square { background: var(--brand-blue); flex: none; }
  .brand-mark--large { left: 354px; top: 160px; width: 494px; height: 272px; justify-content: center; font-size: 44px; letter-spacing: 2px; }
  .brand-mark--large .brand-square { width: 44px; height: 44px; }
  .brand-mark--small { left: 206px; top: 812px; width: 226px; height: 121px; justify-content: center; gap: 8px; font-size: 18px; letter-spacing: 0.8px; }
  .brand-mark--small .brand-square { width: 17px; height: 17px; }

  .accent-band {
    position: absolute; left: 198px; top: 525px; width: 805px; height: 50px;
    background: linear-gradient(to right, var(--brand-blue) 0%, var(--brand-light) 50%, var(--brand-blue) 82%, var(--brand-deep) 100%);
  }

  .card-spine { position: absolute; left: 446px; top: 633px; width: 53px; height: 492px; display: flex; flex-direction: column; }
  .spine-top { height: 123px; background: var(--accent-orange); }
  .spine-middle { height: 246px; background: linear-gradient(to bottom, var(--accent-orange), #f4a070 50%, var(--brand-blue)); }
  .spine-bottom { height: 123px; background: var(--brand-blue); }

  .contact-name { position: absolute; right: 218px; top: 682px; font-size: 30px; font-weight: 700; letter-spacing: 3px; color: var(--accent-orange); }
  .contact-title { position: absolute; right: 218px; top: 722px; font-size: 15px; letter-spacing: 1.5px; }

  .contact-lines { position: absolute; text-align: right; font-size: 18px; letter-spacing: 2px; line-height: 25px; white-space: nowrap; }
  .contact-phone { right: 286px; top: 856px; }
  .contact-web { right: 286px; top: 955px; line-height: 30px; }
  .contact-address { right: 278px; top: 1072px; font-size: 15.5px; letter-spacing: 1.3px; }

  .contact-icon {
    position: absolute; width: 52px; height: 52px; background: var(--icon-blue);
    display: flex; align-items: center; justify-content: center;
  }
  .contact-icon svg { width: 34px; height: 34px; }
  .icon-phone { left: 932px; top: 854px; }
  .icon-web { left: 931px; top: 958px; }
  .icon-pin { left: 934px; top: 1056px; width: 49px; height: 48px; }
</style>
</head>
<body>
  <div class="brand-mark brand-mark--large"><span class="brand-square"></span>KRT BUILDERS, INC.</div>

  <div class="accent-band" role="img" aria-label="Horizontal blue accent band"></div>

  <div class="brand-mark brand-mark--small"><span class="brand-square"></span>KRT BUILDERS, INC.</div>

  <div class="card-spine">
    <div class="spine-top"></div>
    <div class="spine-middle" role="img" aria-label="Orange to blue accent band"></div>
    <div class="spine-bottom"></div>
  </div>

  <div class="contact-name">Marco T. Rinaldi</div>
  <div class="contact-title">Managing Director &amp; CEO</div>

  <div class="contact-lines contact-phone">212-555-0147<br>212-555-0183</div>
  <div class="contact-icon icon-phone">
    <svg viewBox="0 0 34 34" fill="none" stroke="#fff" stroke-width="2.2" stroke-linecap="round">
      <path d="M9 6c-2 1-3 3-2 6 2 7 7 13 14 15 3 1 5 0 6-2l-4-4-3 2c-3-1-6-5-7-8l2-3-4-6z" fill="#fff" stroke="none"/>
      <path d="M19 9a7 7 0 0 1 6 6M19 4a12 12 0 0 1 11 11"/>
    </svg>
  </div>

  <div class="contact-lines contact-web">marco@krtbuilders.com<br>www.krtbuilders.com</div>
  <div class="contact-icon icon-web">
    <svg viewBox="0 0 34 34" fill="none" stroke="#fff" stroke-width="2">
      <circle cx="17" cy="17" r="13"/>
      <ellipse cx="17" cy="17" rx="6" ry="13"/>
      <path d="M4 17h26M6 10h22M6 24h22M17 4v26"/>
    </svg>
  </div>

  <div class="contact-lines contact-address">118 Harbor Street-Bayonne, New Jersey 07002</div>
  <div class="contact-icon icon-pin">
    <svg viewBox="0 0 34 34">
      <path d="M17 3a10 10 0 0 0-10 10c0 8 10 18 10 18s10-10 10-18A10 10 0 0 0 17 3z" fill="#fff"/>
      <circle cx="17" cy="13" r="4" fill="#29a8e0"/>
    </svg>
  </div>
</body>
</html>
```